I want to thank you very much for all your great designs. It was a really tough choice, but I have finally chosen a winner. I have been very happy with this process and very pleased with all the great choices I was given. I will definitely refer this company to my friends and tell them that they will get exactly what they are looking for from many, very talented designers. Thanks again! Dana
Hello All.
When doing that additional return address label,
Include:
- Logo
- Company Name
- Address
- Design Concept
- Size: 4"X3" (inches) return label
Thanks
Hello Designers! Great work that I'm seeing! If I have starred one of your designs, you should have received private messages regarding them by now. If not, please message me.
Can you please be sure to resubmit those designs with the changes I have requested because if I starred it, I'm considering it as my choice.
Don't forget to review the general comments in case I didn't add those things in your private messages.
One thing I wanted to add to the general comments is the fact that I somehow want "The Builder's Coverage Advisors" to be incorporated large on the back of the cards.
After I get the updated designs and I will re-star them. I would then like to start receiving the stationery layouts from the top designs I pick. Besides the letterhead and #10 return envelope I will also need a design for a return address label/sticker for a large 9X11 envelope.
Thanks for your participation. I look for to the updated designs. Dana
Hi. Thanks so much for all your designs. Just a couple of general comments.
I do like the more colorful cards using the gold as an accent only. I prefer the blue and black and white more for large sections or entire backgrounds.
I would like either spaces or periods between all the phone numbers, please. example: 555.418.3927 or 555 418 3927
License number can simply be License# .......
I haven't decided if I like the symbols next to the phone, fax, email, web yet. Can I see some different options instead of symbols so I can decide.
Thanks again for your time and great work. I look forward to choosing the winning design. Dana
I haven't decided if I like the symbols next to the phone, fax, email, web. Can I see some different options instead of symbols.
Thanks for your time and great work. I look forward to choosing the winning design. Dana
RT/PHW/NC Team
#8 I like this one too. Like the added info on back. Also can you please add the license number so I can see that on there. We have to advertise our insurance license for the company and individuals. Thanks
#2 I like this design. Please add & refer to the information requested on card in the design request area and the comments section for information on what info I want on the back. I'd like to see it with all my data, please. Please also add spacing or characters on the phone numbers. Thanks so much.

```html
<!DOCTYPE html>
<html lang="en">
<head>
<meta charset="utf-8">
<title>Halvern Insurance Services – Business Card</title>
<link rel="stylesheet" href="https://fonts.googleapis.com/css2?family=Arimo:ital,wght@0,400;0,700;1,700&display=swap">
<style>
  :root{
    --page:#e9e6e1;
    --ink:#1a1a1a;
    --blue:#1f6fae;
    --blue-deep:#0d3f6e;
    --blue-light:#3a9ad9;
    --gold:#b8965a;
    --white:#ffffff;
    --muted:#555555;
  }
  *{box-sizing:border-box;margin:0;padding:0}
  html,body{width:1200px;height:770px;overflow:hidden}
  body{background:var(--page);font-family:'Arimo',Arial,sans-serif;position:relative;color:var(--ink)}
  .card{position:absolute;width:620px;height:354px;border-radius:14px;overflow:hidden;box-shadow:0 10px 26px rgba(0,0,0,.22)}

  /* front */
  .card-front{left:40px;top:40px;background:var(--white)}
  .brand{position:absolute;display:flex;align-items:center;gap:10px}
  .brand-dot{width:34px;height:34px;border-radius:50%;background:var(--blue)}
  .brand-name{font-weight:700;font-size:50px;line-height:1;letter-spacing:-1px}
  .brand-sub{font-weight:700;font-size:19px;line-height:1}
  .card-front .brand-block{position:absolute;left:300px;top:22px}
  .card-front .brand{position:static}
  .card-front .brand-name{color:var(--ink)}
  .card-front .brand-sub{color:var(--blue);margin-left:44px;margin-top:2px}
  .tagline{font-style:italic;font-weight:700;font-size:11px}
  .card-front .tagline{color:var(--ink);margin-left:44px;margin-top:4px}
  .gold-tab{position:absolute;right:0;top:102px;width:14px;height:22px;background:var(--gold)}
  .person{position:absolute;right:30px;top:108px;text-align:right}
  .person-name{font-size:21px;color:var(--blue);font-weight:400}
  .person-title{font-size:11px;color:var(--muted)}
  .address{position:absolute;right:30px;top:162px;text-align:right;font-size:12px;line-height:1.45;color:var(--ink)}
  .contact-list{position:absolute;right:30px;top:210px;list-style:none;font-size:12px;line-height:1.45;text-align:right}
  .contact-list li{display:flex;justify-content:flex-end;align-items:center;gap:6px}
  .contact-list svg{width:11px;height:11px;fill:var(--ink)}
  .web-list{position:absolute;left:250px;top:266px;list-style:none;font-size:12px;line-height:1.5}
  .web-list li{display:flex;justify-content:flex-end;align-items:center;gap:6px}
  .web-list svg{width:11px;height:11px;fill:var(--ink)}
  .license{position:absolute;right:30px;top:296px;font-size:13px;font-weight:700;color:var(--blue)}

  /* back */
  .card-back{left:540px;top:396px;background:linear-gradient(125deg,var(--blue-light) 0%,var(--blue) 45%,var(--blue-deep) 100%);color:var(--white)}
  .card-back .brand{left:310px;top:26px}
  .card-back .brand-dot{background:var(--white);width:40px;height:40px}
  .card-back .brand-name{color:var(--white);font-size:46px}
  .card-back .brand-sub{position:absolute;left:360px;top:74px;color:var(--white);font-size:18px}
  .card-back .tagline-top{position:absolute;left:360px;top:96px;font-size:11px;font-style:italic;font-weight:700}
  .phone-big{position:absolute;right:26px;top:150px;font-size:29px;font-weight:700}
  .web-big{position:absolute;right:26px;top:188px;font-size:17px;font-weight:700}
  .services{position:absolute;left:28px;top:150px;list-style:none;font-size:17px;line-height:1.17}
  .services li{display:flex;align-items:center;gap:8px}
  .services svg{width:13px;height:13px}
  .band{position:absolute;left:0;right:0;bottom:0;height:44px;background:var(--blue-deep);display:flex;align-items:center;padding-left:28px;font-style:italic;font-weight:700;font-size:14px}
</style>
</head>
<body>

<section class="card card-front" aria-label="Business card front">
  <div class="brand-block">
    <div class="brand"><span class="brand-dot"></span><span class="brand-name">Halvern</span></div>
    <div class="brand-sub">Insurance Services</div>
    <div class="tagline">The Builder's Coverage Advisors</div>
  </div>
  <span class="gold-tab"></span>
  <div class="person">
    <div class="person-name">Dana Halvern</div>
    <div class="person-title">President</div>
  </div>
  <address class="address" style="font-style:normal">2290 Linden Crest Road #204<br>Alder Vale, CA 90417</address>
  <ul class="contact-list">
    <li>555.418.3927 <svg viewBox="0 0 24 24"><path d="M6.6 10.8a15 15 0 0 0 6.6 6.6l2.2-2.2c.3-.3.7-.4 1-.2 1.1.4 2.3.6 3.6.6.6 0 1 .4 1 1V20c0 .6-.4 1-1 1A17 17 0 0 1 3 4c0-.6.4-1 1-1h3.5c.6 0 1 .4 1 1 0 1.3.2 2.5.6 3.6.1.3 0 .7-.2 1z"/></svg></li>
    <li>555.306.7142 <svg viewBox="0 0 24 24"><path d="M6 3h10v5H6zM3 9h18v9h-3v3H6v-3H3zm5 6v4h8v-4z"/></svg></li>
    <li>555.418.3950 <svg viewBox="0 0 24 24"><path d="M7 1h10a2 2 0 0 1 2 2v18a2 2 0 0 1-2 2H7a2 2 0 0 1-2-2V3a2 2 0 0 1 2-2zm0 3v14h10V4z"/></svg></li>
  </ul>
  <ul class="web-list">
    <li>Dana@HalvernInsure.com <svg viewBox="0 0 24 24"><path d="M2 5h20v14H2zm2 2v.5l8 5 8-5V7z"/></svg></li>
    <li>www.HalvernInsure.com <svg viewBox="0 0 24 24"><path d="M12 2a10 10 0 1 0 0 20 10 10 0 0 0 0-20zm0 2c1 1.2 1.8 3.3 2 6h-4c.2-2.7 1-4.8 2-6zM4.1 10h3.9c.1-2 .6-3.9 1.3-5.3A8 8 0 0 0 4.1 10zm0 4a8 8 0 0 0 5.2 5.3C8.6 17.9 8.1 16 8 14zM10 14c.2 2.7 1 4.8 2 6 1-1.2 1.8-3.3 2-6zm6 0c-.1 2-.6 3.9-1.3 5.3A8 8 0 0 0 19.9 14zm3.9-4a8 8 0 0 0-5.2-5.3c.7 1.4 1.2 3.3 1.3 5.3z"/></svg></li>
  </ul>
  <div class="license">License No# 0479216</div>
</section>

<section class="card card-back" aria-label="Business card back">
  <div class="brand"><span class="brand-dot"></span><span class="brand-name">Halvern</span></div>
  <div class="brand-sub">Insurance Services</div>
  <div class="tagline-top">The Builder's Coverage Advisors</div>
  <ul class="services">
    <li><svg viewBox="0 0 16 16"><circle cx="8" cy="8" r="7" fill="#fff"/><path d="M4.5 8.2l2.3 2.3 4.7-4.8" stroke="#1f6fae" stroke-width="1.8" fill="none"/></svg>General Liability</li>
    <li><svg viewBox="0 0 16 16"><circle cx="8" cy="8" r="7" fill="#fff"/><path d="M4.5 8.2l2.3 2.3 4.7-4.8" stroke="#1f6fae" stroke-width="1.8" fill="none"/></svg>Worker's Compensation</li>
    <li><svg viewBox="0 0 16 16"><circle cx="8" cy="8" r="7" fill="#fff"/><path d="M4.5 8.2l2.3 2.3 4.7-4.8" stroke="#1f6fae" stroke-width="1.8" fill="none"/></svg>Commercial Auto</li>
    <li><svg viewBox="0 0 16 16"><circle cx="8" cy="8" r="7" fill="#fff"/><path d="M4.5 8.2l2.3 2.3 4.7-4.8" stroke="#1f6fae" stroke-width="1.8" fill="none"/></svg>Course of Construction</li>
    <li><svg viewBox="0 0 16 16"><circle cx="8" cy="8" r="7" fill="#fff"/><path d="M4.5 8.2l2.3 2.3 4.7-4.8" stroke="#1f6fae" stroke-width="1.8" fill="none"/></svg>Equipment/Tools</li>
    <li><svg viewBox="0 0 16 16"><circle cx="8" cy="8" r="7" fill="#fff"/><path d="M4.5 8.2l2.3 2.3 4.7-4.8" stroke="#1f6fae" stroke-width="1.8" fill="none"/></svg>Bonds</li>
    <li><svg viewBox="0 0 16 16"><circle cx="8" cy="8" r="7" fill="#fff"/><path d="M4.5 8.2l2.3 2.3 4.7-4.8" stroke="#1f6fae" stroke-width="1.8" fill="none"/></svg>EPLI</li>
    <li><svg viewBox="0 0 16 16"><circle cx="8" cy="8" r="7" fill="#fff"/><path d="M4.5 8.2l2.3 2.3 4.7-4.8" stroke="#1f6fae" stroke-width="1.8" fill="none"/></svg>BOP</li>
  </ul>
  <div class="phone-big">555-418-3927</div>
  <div class="web-big">www.HalvernInsure.com</div>
  <div class="band">The Builder's Coverage Advisors</div>
</section>

</body>
</html>
```